A brand new wordpress website for my business which will replace my current site www.harbornetcall.com.au, As i rank quite well in google will it be ok to keep my current URL's. I sell the following service and products

1. Voip Provider (Main service) we sell directly the the end user but also we would like to get resellers and agents to sell our services. agents selling our brand resellers sell our services branded as theirs
2. Hosted Pbx (main service) home page must push this service explaining the benifits and features that come with a hosted pbx, we also have business plans based on number of extensions (phones) the customer requires
3. Tornax IP Pbx (product) only selling IP Pbx and selected software
4. Velbox IP Pbx (product)
5. Quorvin IP Phones (this is the main VoIP phone we sell)
6. lumora phones (to be on a landing page only not apart of the main site)
7. selected headsets from Dravensonic (products)
8. Meridal Conference phone (VoIP model only)
9. we can supply fax to email service

we would like a support page with user guides (step by step instructions on our products and services and FAQ's about all products and services

we have a carrier grade softswitch (telco billing system) z7ledger http://www.pinwheelledger.org this system has a ticketing system, customer and agent login I would like a URL link from our website so customers can login to this system. also it is possible to skin z7ledger to look like our website

VoIP business plans

$0 per month
call rate .12c land line calls
.24c per minute mobile calls

$25 per month
250 Free local land line calls
call rate is .10c land line calls .22c per minute mobile calls

$50 per month
500 Free local land line calls
call rate .09 land line calls .20c per minute mobile calls

$100 per month
1000 free local land line calls
call rate .08c land line calls .18c per minute mobile calls

all mobile calls are billed per second no flag fall

also require a link to international call rates

We can port your existing telephone number from any carrier or supply new Australian telephone numbers

02, 03, 07, 08, 131, 1300, 1800

Designs i like www.tralcom.com.au and www.orbitelphone.com

I would like the website to be white and bright

Reason: Please use images of the products I sell only

Target Market(s)

business customers only

Industry/Entity Type

Requirements
Must have
• all pages must have its own banner to reflect the product or service we are selling. the home page can automatically change to show all pages with a link straight to the page in question

for example if on the home page the banner for quorvin phone is displaying if someone click on the banner they will be redirected to the quorvin page

Must Be SEO friendly
Nice to have
• shopping cart via paypal for all products but before customer checks out i would like to offer two options

1. Pre configure the item and ship to your address for existing customers
2. would you like a harbor net call technician to attend your office and install the item in person (costs involved $60 call out fee $120 per hours every item sold charge .50 hour and only the one call out fee)

new and existing customers can book service work via the website
1. describe the work required (maybe we need to give a few option)
2. company details
3. pre payment (checkout via paypal) can we put the paypal fees back on to the customer?

```html
<!DOCTYPE html>
<html lang="en">
<head>
<meta charset="utf-8">
<title>Harbor Net Call – Hosted Business PBX</title>
<link href="https://fonts.googleapis.com/css2?family=Open+Sans:ital,wght@0,300;0,400;0,600;0,700;1,400&family=Roboto+Condensed:wght@400;700&display=swap" rel="stylesheet">
<style>
:root{
  --navy:#0b3a80;
  --blue:#1a55a8;
  --bright:#2a7fd6;
  --sky:#4aa3e6;
  --footer:#0f4a92;
  --footer-dark:#0a3270;
  --text:#444;
  --line:#d9dde3;
  --panel:#eceef1;
  --white:#fff;
}
*{margin:0;padding:0;box-sizing:border-box}
html,body{width:683px;height:1200px;overflow:hidden;background:var(--white)}
body{position:relative;font-family:"Open Sans",Arial,sans-serif;color:var(--text);font-size:8px}
.abs{position:absolute}

/* header */
.header{left:0;top:0;width:683px;height:54px;background:linear-gradient(#fff,#f3f4f6)}
.logo{left:85px;top:14px;display:flex;align-items:center;gap:6px}
.logo-mark{width:12px;height:12px;background:var(--blue)}
.logo-name{font-weight:700;font-size:17px;color:var(--navy);letter-spacing:-.3px}
.help{right:88px;top:18px;text-align:right;color:var(--navy);font-weight:700}
.help small{display:block;font-size:7px;color:#333}
.help strong{font-size:12px}
.help svg{position:absolute;right:-12px;top:7px}

/* nav */
.nav{left:0;top:54px;width:683px;height:33px;background:linear-gradient(#fafafa,#dfe2e6);border-top:1px solid #d0d4da;border-bottom:1px solid #c8ccd2}
.nav a{position:absolute;top:0;height:32px;line-height:32px;font-size:8.5px;font-weight:700;color:#3a4654;text-decoration:none;font-family:"Roboto Condensed",sans-serif;letter-spacing:.3px}
.nav a.active{color:var(--blue);background:#fff;padding:0 8px;border-left:1px solid #cfd3d9;border-right:1px solid #cfd3d9;border-top:2px solid var(--blue)}
.signup{left:516px;top:3px;width:81px;height:26px;background:var(--navy);color:#fff;font:700 12px/26px "Roboto Condensed",sans-serif;text-align:center;border-radius:2px}

/* hero */
.hero{left:0;top:87px;width:683px;height:198px;background:radial-gradient(ellipse at 35% 40%,var(--sky),var(--bright) 35%,var(--navy) 90%)}
.hero-photo{left:85px;top:12px;width:278px;height:173px;border-radius:14px;background:radial-gradient(ellipse at 50% 55%,#3a3f46,#1c2026 55%,transparent 72%)}
.hero-title{left:396px;top:28px;color:#fff;font-weight:300;font-size:19px;white-space:nowrap}
.hero-sub{left:397px;top:55px;color:#fff;font-weight:700;font-size:8.5px;white-space:nowrap}
.ticks{left:397px;top:76px;list-style:none;color:#fff;font:400 8px "Roboto Condensed",sans-serif}
.ticks li{height:14.5px;display:flex;align-items:center;gap:6px;white-space:nowrap}
.btn-light{left:398px;top:148px;width:155px;height:28px;background:linear-gradient(#fff,#e3e6ea);color:var(--navy);font:700 9.5px/28px "Roboto Condensed",sans-serif;text-align:center;box-shadow:0 2px 3px rgba(0,0,0,.3)}

/* intro panel */
.intro{left:74px;top:285px;width:536px;height:227px;background:#fff;box-shadow:0 2px 6px rgba(0,0,0,.15)}
.card{width:143px;height:90px;border:1px solid var(--line);background:linear-gradient(#fff,#f1f2f4);padding:6px 7px}
.card h3{font:700 9.5px/12px "Open Sans",sans-serif;color:var(--blue);margin-bottom:2px;white-space:nowrap;position:relative;z-index:1}
.card p{font-size:6.2px;line-height:8.4px;color:#333;width:92px}
.card ul{list-style:none;font-size:6.2px;line-height:8.4px;width:92px;color:#333}
.card ul li::before{content:"» ";color:var(--blue)}
.card .thumb{position:absolute;right:6px;top:10px;width:36px;height:54px;border-radius:6px;background:linear-gradient(160deg,#6b6f76,#1f2227)}
.btn-dark{position:absolute;left:7px;bottom:5px;width:66px;height:12px;background:var(--navy);color:#fff;font:700 6px/12px "Open Sans",sans-serif;padding-left:5px;white-space:nowrap}
.btn-dark::after{content:"";position:absolute;right:5px;top:3px;border:3px solid transparent;border-left:4px solid #fff;border-right:0}
.intro-copy{left:323px;top:17px;width:210px}
.intro-copy h2{font-size:7.6px;font-weight:700;color:#222;line-height:10px}
.intro-copy .lead{font-size:7.6px;color:var(--blue);line-height:10.5px;margin:4px 0 10px}
.intro-copy ul{list-style:none;font-size:5.9px;color:#333}
.intro-copy li{height:15.6px;padding-left:10px;position:relative;white-space:nowrap}
.intro-copy li::before{content:"»";position:absolute;left:0;color:var(--blue);font-weight:700}
.btn-cta{left:324px;top:176px;width:173px;height:27px;background:var(--navy);color:#fff;font:700 8.5px/27px "Roboto Condensed",sans-serif;text-align:center;box-shadow:0 2px 3px rgba(0,0,0,.3)}

/* plans */
.plans-bg{left:0;top:532px;width:683px;height:248px;background:var(--panel)}
.plans-tab{left:262px;top:522px;width:161px;height:28px;background:#fff;box-shadow:0 1px 3px rgba(0,0,0,.2);color:var(--blue);font:700 11px/28px "Roboto Condensed",sans-serif;text-align:center}
.intl{right:95px;top:537px;color:var(--navy);font-size:6.5px;text-decoration:underline}
.billing{right:95px;top:550px;font-size:6px;color:#444}
.row-label{left:89px;width:93px;height:45px;background:var(--navy);color:#fff;font:400 9.5px "Roboto Condensed",sans-serif;display:flex;align-items:center;gap:8px;padding-left:8px;white-space:nowrap}
.row-label.mobile{background:var(--blue)}
.plan{background:#fff;border:1px solid #9fc9e8;text-align:center}
.plan .price{height:36px;display:flex;align-items:center;justify-content:center;background:linear-gradient(#fff,#e1e5ea);color:var(--blue);font:700 12px "Roboto Condensed",sans-serif;border-bottom:1px solid var(--line)}
.plan .price small{font-size:8.5px;margin-left:3px}
.plan.featured .price{background:linear-gradient(var(--blue),var(--navy));color:#fff}
.plan .cell{position:absolute;left:0;width:100%;height:45px;display:flex;flex-direction:column;align-items:center;justify-content:center;color:var(--navy)}
.plan .cell b{font:700 11px "Roboto Condensed",sans-serif}
.plan .cell span{font-size:5.5px;color:#333;font-weight:400;font-family:"Open Sans",sans-serif}
.plan .cell.alt{background:#f7f8fa;border-top:1px solid var(--line)}
.plan .go{position:absolute;left:4px;right:4px;bottom:0;height:18px;background:linear-gradient(var(--blue),var(--navy));color:#fff;font:700 9px/18px "Roboto Condensed",sans-serif}
.ribbon{right:-4px;top:-8px;width:36px;height:14px;background:#19a3b6;color:#fff;font-size:5px;font-weight:700;line-height:14px;transform:rotate(40deg)}

/* testimonials */
.clients-title{left:0;width:683px;top:795px;text-align:center;color:var(--navy);font:700 11px "Roboto Condensed",sans-serif}
.title-rule{left:200px;top:812px;width:283px;height:1px;background:linear-gradient(90deg,transparent,#ccc,transparent)}
.quote{left:191px;top:832px;width:340px;text-align:center;font-style:italic;color:#888;font-size:8px;line-height:13.5px}
.qmark{font:700 34px Georgia,serif;color:#c9ccd1}
.avatar{top:896px;width:27px;height:29px;border:1px solid #bbb;background:linear-gradient(#d7d9dc,#9da2a8)}
.avatar.current{border-color:var(--blue);background:linear-gradient(#cdd7e3,#7d8fa6)}
.client-name{left:298px;top:930px;font-size:6.5px;color:var(--navy);font-weight:700}

/* promo */
.promo{left:0;top:955px;width:683px;height:73px;background:linear-gradient(#fff,#eef0f3);border-top:2px solid #d7dadf}
.promo-photo{left:85px;top:-8px;width:92px;height:80px;border-radius:8px;background:linear-gradient(150deg,#8a8f96,#2a2e34)}
.promo-head{left:184px;top:19px;color:var(--navy);font:700 13.5px "Roboto Condensed",sans-serif;white-space:nowrap}
.promo-sub{left:242px;top:36px;color:#2b3440;font:700 13px "Roboto Condensed",sans-serif;white-space:nowrap}
.promo-btn{left:502px;top:20px;width:91px;height:25px;background:var(--navy);color:#fff;font:700 8px/25px "Open Sans",sans-serif;padding-left:11px}
.promo-btn::after{content:"";position:absolute;right:9px;top:8.5px;border:4px solid transparent;border-left:5px solid #fff;border-right:0}

/* footer */
.footer{left:0;top:1028px;width:683px;height:152px;background:var(--footer)}
.fcol{top:12px;color:#fff}
.fcol h4{font:400 10px "Roboto Condensed",sans-serif;letter-spacing:.5px;margin-bottom:7px}
.fcol ul{list-style:none;font-size:6.5px;color:#dbe6f5}
.fcol li{height:13.3px;padding-left:10px;position:relative;white-space:nowrap}
.fcol li::before{content:"»";position:absolute;left:0;color:#9bb8df}
.social li{padding-left:16px;height:15.5px;display:flex;align-items:center}
.social li::before{content:"";width:10px;height:10px;border-radius:50%;background:#dbe6f5;top:0.5px}
.contact p{font-size:6.5px;color:#dbe6f5;line-height:9px;margin-bottom:5px}
.contact .ci{display:flex;gap:8px;align-items:flex-start;font-size:6.5px;color:#dbe6f5;line-height:9px;margin-bottom:7px}
.contact .ci i{flex:none;width:12px;height:12px;background:#2f67ad;display:flex;align-items:center;justify-content:center}
.live{left:502px;top:1155px;width:115px;height:25px;background:var(--footer-dark);color:#fff;font:700 11px/25px "Roboto Condensed",sans-serif;padding-left:16px}
.copy{left:0;top:1180px;width:683px;height:20px;background:var(--footer-dark);color:#8ea8cc;text-align:center;font-size:6px;line-height:20px}
</style>
</head>
<body>

<header class="abs header">
  <div class="abs logo"><span class="logo-mark"></span><span class="logo-name">Harbor Net Call</span></div>
  <div class="abs help"><small>NEED HELP ?</small><strong>1300 482 917</strong>
    <svg width="9" height="11" viewBox="0 0 9 11"><path d="M2 0 L4 3 L3 4.5 Q4 7 5.5 8 L7 7 L9 9.5 L7.5 11 Q1 9 0 1.5Z" fill="#0b3a80"/></svg>
  </div>
</header>

<nav class="abs nav">
  <a class="active" style="left:85px">HOME</a>
  <a style="left:134px">PRODUCTS</a>
  <a style="left:190px">ABOUT</a>
  <a style="left:231px">HOSTED PBX</a>
  <a style="left:295px">CONTACT US</a>
  <a style="left:360px">TELEPHONE SYSTEMS</a>
  <a style="left:474px">PLANS</a>
  <div class="abs signup">&#9787; SIGNUP</div>
</nav>

<section class="abs hero">
  <div class="abs hero-photo" role="img" aria-label="Desk IP phone with handset and display screen"></div>
  <h1 class="abs hero-title">Hosted Business PBX</h1>
  <p class="abs hero-sub">Full-Featured and Friendly Support</p>
  <ul class="abs ticks">
    <li><svg width="9" height="8"><path d="M1 4 L3.5 6.5 L8 1" stroke="#fff" stroke-width="1.8" fill="none"/></svg>As Many Extensions as You Need</li>
    <li><svg width="9" height="8"><path d="M1 4 L3.5 6.5 L8 1" stroke="#fff" stroke-width="1.8" fill="none"/></svg>Completely Customized Auto Attendant</li>
    <li><svg width="9" height="8"><path d="M1 4 L3.5 6.5 L8 1" stroke="#fff" stroke-width="1.8" fill="none"/></svg>Send Voicemail To Your Email as an Wav File</li>
    <li><svg width="9" height="8"><path d="M1 4 L3.5 6.5 L8 1" stroke="#fff" stroke-width="1.8" fill="none"/></svg>All Extensions on any Conference</li>
  </ul>
  <div class="abs btn-light">MORE FEATURES &amp; BENEFITS &#9656;</div>
</section>

<section class="abs intro">
  <div class="abs card" style="left:11px;top:15px">
    <h3>VoIP Plans</h3>
    <p>Premium call quality with Included Standard Calls. We reduce your business costs.</p>
    <div class="thumb" role="img" aria-label="Black desk phone"></div>
    <div class="btn-dark">VIEW PLANS</div>
  </div>
  <div class="abs card" style="left:162px;top:15px">
    <h3>Hosted Pbx</h3>
    <ul><li>Completely Customized Auto Attendant</li><li>Send Voicemail To Your Email as an Wav File</li></ul>
    <div class="thumb" role="img" aria-label="IP desk phone"></div>
    <div class="btn-dark">MORE BENEFITS</div>
  </div>
  <div class="abs card" style="left:11px;top:118px">
    <h3>Headsets</h3>
    <p>The Dravensonic DS60 allows you to multi-task more easily – whether that is making notes or using your PC whilst on a phone call.</p>
    <div class="thumb" role="img" aria-label="Wireless office headset" style="background:linear-gradient(160deg,#d4d6da,#8f949b)"></div>
    <div class="btn-dark">VIEW MORE</div>
  </div>
  <div class="abs card" style="left:162px;top:118px">
    <h3>Conference Phone</h3>
    <p>Neque porro quisquam est qui dolorem ipsum quia dolor sit amet,</p>
    <div class="thumb" role="img" aria-label="Conference speaker phone" style="top:22px;height:46px"></div>
    <div class="btn-dark">PRODUCTS</div>
  </div>
  <div class="abs intro-copy">
    <h2>Small to Medium Business Phone Systems &amp;<br>Hosted PBX Solutions</h2>
    <p class="lead">Harbor Net Call can get you started with a feature rich and low upfront cost VoIP Phone System.</p>
    <ul>
      <li>Low upfront phone system costs to get started - from $0.09c</li>
      <li>Self manage your VoIP phone system via friendly web interface</li>
      <li>IPhone/laptop phone system integration</li>
      <li>No on site technician charges</li>
      <li>Always be up to date with phone system technology</li>
      <li>Link multiple office/home together as one</li>
    </ul>
  </div>
  <div class="abs btn-cta">CLICK HERE TO FIND OUT HOW IT WORKS &#9656;</div>
</section>

<div class="abs plans-bg"></div>
<div class="abs plans-tab">VOIP BUSINESS PLANS</div>
<a class="abs intl">international call rates &#9656;</a>
<p class="abs billing">*all mobile calls are billed per second</p>

<div class="abs row-label" style="top:625px">
  <svg width="12" height="14" viewBox="0 0 9 11"><path d="M2 0 L4 3 L3 4.5 Q4 7 5.5 8 L7 7 L9 9.5 L7.5 11 Q1 9 0 1.5Z" fill="#fff"/></svg>LAND LINE CALLS</div>
<div class="abs row-label mobile" style="top:675px">
  <svg width="10" height="15"><rect x="1" y="1" width="8" height="13" rx="1.5" fill="none" stroke="#fff" stroke-width="1.4"/><rect x="3" y="3" width="4" height="7" fill="#fff"/></svg>MOBILE CALLS</div>

<div class="abs plan" style="left:184px;top:584px;width:92px;height:178px">
  <div class="price">$0<small>per month</small></div>
  <div class="cell" style="top:41px"><b>.12c</b><span>Call rate</span></div>
  <div class="cell alt" style="top:91px"><b>.24c</b><span>Call rate</span></div>
  <div class="go">FREE PLAN</div>
</div>
<div class="abs plan" style="left:279px;top:575px;width:106px;height:187px">
  <div class="price" style="height:45px">$25<small>per month</small></div>
  <div class="cell" style="top:50px"><b>250 Free</b><span>local calls</span><b>.10c <span>Call rate</span></b></div>
  <div class="cell alt" style="top:100px"><b>.22c</b><span>Call rate</span></div>
  <div class="go">GET THIS PLAN</div>
</div>
<div class="abs plan" style="left:389px;top:584px;width:93px;height:178px">
  <div class="price">$50<small>per month</small></div>
  <div class="cell" style="top:41px"><b>500 Free</b><span>local calls</span><b>.09c <span>Call rate</span></b></div>
  <div class="cell alt" style="top:91px"><b>.20c</b><span>Call rate</span></div>
  <div class="go">GET THIS PLAN</div>
</div>
<div class="abs plan featured" style="left:484px;top:575px;width:109px;height:187px">
  <div class="price" style="height:45px">$100<small>per month</small></div>
  <div class="abs ribbon">BEST VALUE</div>
  <div class="cell" style="top:50px"><b>1000 Free</b><span>local calls</span><b>.08c <span>Call rate</span></b></div>
  <div class="cell alt" style="top:100px"><b>.18c</b><span>Call rate</span></div>
  <div class="go">GET THIS PLAN</div>
</div>

<h2 class="abs clients-title">READ WHAT OUR CLIENTS SAYS...</h2>
<div class="abs title-rule"></div>
<div class="abs qmark" style="left:178px;top:818px">&ldquo;</div>
<p class="abs quote">Lorem Ipsum is simply dummy text of the printing&nbsp; Lorem is and typesetting industry.<br>Lorem Ipsum is simply dummy text of the printing&nbsp; Lorem is<br>and typesetting industry.</p>
<div class="abs qmark" style="left:418px;top:848px">&rdquo;</div>
<div class="abs avatar current" style="left:305px" role="img" aria-label="Client portrait"></div>
<div class="abs avatar" style="left:339px" role="img" aria-label="Client portrait"></div>
<div class="abs avatar" style="left:373px" role="img" aria-label="Client portrait"></div>
<div class="abs avatar" style="left:406px" role="img" aria-label="Client portrait"></div>
<p class="abs client-name">- Owen Pratley</p>

<section class="abs promo">
  <div class="abs promo-photo" role="img" aria-label="Grey desk IP phone"></div>
  <p class="abs promo-head">FREE KLARIN 300 PHONES ON A 24 MONTH PLAN</p>
  <p class="abs promo-sub">Special HNC over limited time only.</p>
  <div class="abs promo-btn">FIND OUT MORE</div>
</section>

<footer class="abs footer">
  <div class="abs fcol" style="left:87px">
    <h4>QUICK LINKS</h4>
    <ul><li>Home</li><li>About</li><li>Hosted PBX</li><li>Contact Us</li><li>Telephone Systems</li><li>Plans &amp; Signup</li><li>Terms and privacy policy</li><li>Sitemap</li></ul>
  </div>
  <div class="abs fcol" style="left:223px">
    <h4>PRODUCTS</h4>
    <ul><li>IP Telephones</li><li>Conference Phone</li><li>Headsets</li><li>Routers &amp; Modems</li><li>Switches</li><li>Velbox IP Telephone Systems</li><li>Tornax Quadro</li><li>Dect Phones</li></ul>
  </div>
  <div class="abs fcol social" style="left:371px">
    <h4>SOCIAL MEDIA</h4>
    <ul><li>Friendwall</li><li>Chirpline</li><li>Searchly Plus</li><li>Pinboardy</li><li>Workweave</li></ul>
  </div>
  <div class="abs fcol contact" style="left:502px;width:110px">
    <h4>QUICK CONTACT</h4>
    <p>Have questions? Don't hesitate to contact us</p>
    <div class="ci"><i><svg width="6" height="8"><path d="M3 8 L0.5 3.5 A2.5 2.5 0 1 1 5.5 3.5Z" fill="#fff"/></svg></i>45 Wattle Lane, Suite #3<br>Kellyvale, NY 10712</div>
    <div class="ci"><i><svg width="7" height="8" viewBox="0 0 9 11"><path d="M2 0 L4 3 L3 4.5 Q4 7 5.5 8 L7 7 L9 9.5 L7.5 11 Q1 9 0 1.5Z" fill="#fff"/></svg></i>1300 482 917 /0415260338</div>
    <div class="ci"><i><svg width="8" height="6"><rect x=".5" y=".5" width="7" height="5" fill="none" stroke="#fff"/><path d="M.5 .5 L4 3.5 L7.5 .5" stroke="#fff" fill="none"/></svg></i>info@harbornetcall.com</div>
  </div>
</footer>
<div class="abs live">LIVE HELP
  <svg class="abs" style="right:8px;top:-8px" width="34" height="22"><ellipse cx="14" cy="9" rx="12" ry="7" fill="#dbe6f5"/><ellipse cx="24" cy="13" rx="9" ry="6" fill="#9bb8df"/></svg>
</div>
<div class="abs copy">Copyright © 2012, Harbor Net Call . All Rights Reserved.</div>

</body>
</html>
```